DOVR Business Card Design Project

Company Name: DOVR (Dove Operational Versatile Resources) JLT.
Office Address: Office No 218, Saffron Crest Tower, Palmera Bay Towers, Dubai, U.A.E
Company line of business:
1) Currently we have a POS solution for retail outlets like duty free shops, supermarkets, department stores etc... The solution is deployed in Harbor Gate Retail on 350 POS and in Coralline Port Retail on 100 POS. So our main line of business is the deployment of this solution in retail outlets locally or regionally. We have already deployed the solution in India and Australia.
2) Integration of other third party POS systems with an online credit authorization netwotk in the UAE. This will enable POS applications to connect directly to the acquiring banks without needing an EFT terminal like Paxoline or Tramodex. The credit card payment is completed at the POS.
3) Other solutions that are targeting retail outlets like mobile POS, queue busting solutions, stock taking solutions using hand held devices, transaction capture systems, etc...
4) Other IT services like support of call center solutions from Bramwell Systems and development of new solutions as per customer requirements.
We need a business card design for the company. We don't have any specific requirements and will eave up to the designers to come up with creative designs. At the moment we still don't have a letter head design and the only thing that we have is the company logo that we will upload shortly.
Updates
Dear All,
I just uploaded the logo source files. I am sorry for the delay.
Regards
Tarek Demirci
I would like the business cards to have the following details:
Company Tel No
Company Fax No
Company Website Address
Employee Name
Employee Title
Employee Mobile Number
Employee Email Address

```html
<!DOCTYPE html>
<html lang="en">
<head>
<meta charset="utf-8">
<title>DOVR Business Card</title>
<link rel="stylesheet" href="https://fonts.googleapis.com/css2?family=Questrial&display=swap">
<style>
  :root {
    --page: #ffffff;
    --silver-light: #ffffff;
    --silver-mid: #e6e7e9;
    --silver-dark: #b9bcc0;
    --charcoal: #3b3d40;
    --ink: #1e1f21;
    --blue-light: #8fd3f2;
    --blue-mid: #2aa7e0;
    --blue-deep: #0f72b4;
    --mark-blue: #1f86c8;
    --white: #ffffff;
  }
  * { margin: 0; padding: 0; box-sizing: border-box; }
  html, body {
    width: 1200px; height: 720px; overflow: hidden;
    background: var(--page);
    font-family: "Questrial", "Century Gothic", sans-serif;
  }
  .card {
    position: absolute; left: 50px; top: 35px;
    width: 1100px; height: 651px;
    border-radius: 46px; overflow: hidden;
    box-shadow: 0 4px 14px rgba(0,0,0,0.18);
  }
  .card-shapes { position: absolute; inset: 0; }
  .brand {
    position: absolute; left: 170px; top: 80px;
    display: flex; align-items: center; gap: 46px;
  }
  .brand-dot {
    width: 190px; height: 190px; border-radius: 50%;
    background: var(--mark-blue);
  }
  .brand-name {
    font-size: 210px; line-height: 1; letter-spacing: 4px;
    color: var(--ink);
  }
  .person-name {
    position: absolute; left: 81px; top: 418px;
    font-size: 40px; letter-spacing: 3px; color: var(--white);
  }
  .person-title {
    position: absolute; left: 276px; top: 476px;
    font-size: 15px; letter-spacing: 1.5px; font-style: italic; color: var(--white);
  }
  .contact-list {
    position: absolute; left: 81px; top: 550px;
    color: var(--white); font-size: 18px; letter-spacing: 1px;
    display: grid; grid-template-columns: 190px auto; row-gap: 12px;
  }
  .company-lines {
    position: absolute; left: 858px; top: 486px;
    color: var(--white); font-size: 20px; font-weight: bold; letter-spacing: 1px;
    line-height: 27px;
  }
</style>
</head>
<body>
  <div class="card">
    <svg class="card-shapes" width="1100" height="651" viewBox="0 0 1100 651" aria-hidden="true">
      <defs>
        <linearGradient id="silver" x1="0" y1="0" x2="0" y2="1">
          <stop offset="0" stop-color="var(--silver-dark)"/>
          <stop offset="0.35" stop-color="var(--silver-light)"/>
          <stop offset="0.8" stop-color="var(--silver-mid)"/>
          <stop offset="1" stop-color="var(--silver-dark)"/>
        </linearGradient>
        <linearGradient id="blue" x1="0" y1="0" x2="0" y2="1">
          <stop offset="0" stop-color="var(--blue-light)"/>
          <stop offset="0.3" stop-color="var(--blue-mid)"/>
          <stop offset="1" stop-color="var(--blue-deep)"/>
        </linearGradient>
      </defs>
      <rect class="top-panel" x="0" y="0" width="1100" height="651" fill="url(#silver)"/>
      <path class="top-band" d="M620 0 H1100 V46 C960 40 800 22 620 0 Z" fill="var(--charcoal)"/>
      <path class="wave-line" d="M0 372 C300 392 700 384 1100 352 V378 C700 404 300 410 0 392 Z" fill="var(--white)"/>
      <path class="bottom-panel" d="M0 392 C300 410 700 404 1100 378 V651 H0 Z" fill="url(#blue)"/>
    </svg>

    <div class="brand">
      <div class="brand-dot"></div>
      <div class="brand-name">DOVR</div>
    </div>

    <div class="person-name">ROWAN ELLIS TAVERA</div>
    <div class="person-title">JOB DESCRIPTION</div>

    <div class="contact-list">
      <span>Mobile Number :</span><span>+971 55 018 2460</span>
      <span>Email Address :</span><span>rowan.tavera@dovr-pbt.com</span>
    </div>

    <div class="company-lines">
      <div>04-3218-30</div>
      <div>04-3218-31</div>
      <div>dovr-pbt.com</div>
    </div>
  </div>
</body>
</html>
```